OpenCart website

We have an existing site that was based on open cart in 2011 but customised heavily. We want a brand new open cart site designed from scratch so we can work on transitioning the existing opencart database over after the project is done

Current site: www.tallowfinchgoods.com

```html
<!DOCTYPE html>
<html lang="en">
<head>
<meta charset="utf-8">
<title>Tallow Finch — Home</title>
<link href="https://fonts.googleapis.com/css2?family=Roboto:wght@400;500;700;900&family=Open+Sans:wght@400;600;700&display=swap" rel="stylesheet">
<style>
:root{
  --red:#e3101b;
  --dark:#1d1d1d;
  --ink:#222;
  --muted:#888;
  --line:#e2e2e2;
  --footer:#141414;
  --white:#fff;
  --soft:#f5f5f5;
}
*{box-sizing:border-box;margin:0;padding:0}
html,body{width:1200px;height:4444px;overflow:hidden}
body{position:relative;background:var(--white);font-family:"Open Sans",sans-serif;color:var(--ink);font-size:13px}
.abs{position:absolute}
a{color:inherit;text-decoration:none}

/* top bar */
.topbar{top:0;left:0;width:1200px;height:52px;border-bottom:1px solid var(--line)}
.topbar .links{left:112px;top:18px;font-size:11px;color:#444;letter-spacing:.3px}
.topbar .links span{margin:0 8px;color:#bbb}
.topbar .prefs{right:112px;top:16px;font-size:11px;color:#444;display:flex;gap:18px;align-items:center}
.flag{display:inline-block;width:14px;height:10px;background:linear-gradient(#c22 50%,#fff 50%);vertical-align:middle;margin-right:4px}

/* header */
.brand{left:112px;top:80px;font-family:"Roboto",sans-serif;font-weight:900;font-size:34px;color:var(--red);letter-spacing:.5px;display:flex;align-items:center;gap:10px;text-transform:uppercase}
.brand .mark{width:20px;height:20px;background:var(--red)}
.search{left:400px;top:98px;width:465px;height:50px;border:1px solid #ccc;display:flex}
.search input{flex:1;border:0;padding:0 16px;font-size:12px;font-family:inherit;color:#999;background:none}
.search button{width:62px;border:0;background:var(--dark);display:flex;align-items:center;justify-content:center}
.account{left:906px;top:104px}
.cart{left:985px;top:104px;display:flex;align-items:center;gap:8px;font-size:11px;font-weight:600}
.cart .badge{position:absolute;left:30px;top:-6px;width:16px;height:16px;border-radius:50%;background:var(--red);color:#fff;font-size:9px;text-align:center;line-height:16px}

/* nav */
.nav{top:184px;left:0;width:1200px;height:44px;background:var(--red)}
.nav ul{position:absolute;left:112px;top:0;height:44px;display:flex;list-style:none;font-family:"Roboto",sans-serif;font-size:12px;font-weight:500;color:#fff;text-transform:uppercase}
.nav li{padding:0 15px;line-height:44px}
.nav li.shop{background:#b30c14;padding:0 12px}
.nav .more{left:1082px;top:14px}

/* hero */
.hero{top:231px;left:0;width:1200px;height:504px;background:linear-gradient(110deg,#3a3a3a 0%,#6b6b66 35%,#b8ad93 60%,#e7dcc3 80%,#8a8273 100%)}
.hero .kicker{left:155px;top:132px;color:#fff;font-size:15px}
.hero h1{left:152px;top:170px;color:#fff;font-family:"Roboto",sans-serif;font-weight:700;font-size:68px;line-height:88px;text-transform:uppercase}
.arrow-btn{width:44px;height:44px;border-radius:50%;border:1px solid rgba(255,255,255,.6);background:rgba(0,0,0,.25);display:flex;align-items:center;justify-content:center}
.dots{display:flex;gap:8px}
.dots i{width:9px;height:9px;border-radius:50%;background:#fff}
.dots i.on{background:var(--red)}

/* promos */
.promo{top:773px;width:475px;height:223px;color:#fff;padding:58px 30px}
.promo h3{font-family:"Roboto",sans-serif;font-weight:700;font-size:26px;line-height:34px;text-transform:uppercase}
.promo p{font-size:13px;margin-top:12px}
.promo .art{position:absolute;right:24px;top:28px;width:190px;height:166px}
.promo.dark{left:112px;background:var(--dark)}
.promo.red{left:613px;background:var(--red)}

/* services */
.services{left:112px;top:1060px;width:261px;height:534px;background:var(--red);padding:40px 26px;color:#fff}
.service{display:flex;gap:18px;margin-bottom:46px}
.service .ico{flex:none;width:44px;height:44px;border-radius:50%;background:#fff;display:flex;align-items:center;justify-content:center}
.service h4{font-size:12px;font-weight:700;text-transform:uppercase;margin:6px 0 10px}
.service p{font-size:12px;line-height:22px}

/* deal */
.section-title{font-family:"Roboto",sans-serif;font-weight:500;font-size:24px;color:var(--ink)}
.deal-nav{right:112px;top:1076px;font-size:12px;color:var(--red)}
.deal-nav b{color:#555;font-weight:400}
.deal-card{left:424px;top:1138px;width:664px;height:444px;border:1px solid var(--line)}
.deal-card .pic{left:36px;top:46px;width:260px;height:350px;border:1px solid var(--line);background:linear-gradient(#fafafa,#e6e6e6)}
.deal-card h3{left:345px;top:82px;font-family:"Roboto",sans-serif;font-weight:500;font-size:22px}
.stars{color:#f2a400;font-size:13px;letter-spacing:1px}
.deal-card .price{left:345px;top:168px;font-size:20px;font-weight:700;color:var(--red)}
.deal-card .desc{left:345px;top:210px;width:290px;font-size:11px;line-height:20px;color:#aaa}
.countdown{left:340px;top:296px;display:flex;gap:15px}
.countdown div{text-align:center;font-size:10px;color:#666}
.countdown span{display:block;width:46px;height:46px;border-radius:50%;background:var(--dark);color:#fff;line-height:46px;font-size:14px;font-weight:700;margin-bottom:6px}

/* products */
.tabs{left:112px;top:1652px;font-family:"Roboto",sans-serif;font-size:20px;font-weight:500;display:flex;gap:50px}
.tabs .on{color:var(--red)}
.pager{right:112px;display:flex;gap:6px}
.pager i{width:22px;height:22px;border:1px solid #ccc;display:flex;align-items:center;justify-content:center;font-style:normal;font-size:12px;color:#777}
.pager i.on{background:#ddd}
.card{width:222px;height:317px;border:1px solid var(--line);background:#fff}
.card .pic{position:absolute;left:26px;top:36px;width:170px;height:170px;border-radius:6px}
.card .off{position:absolute;right:18px;top:10px;font-size:12px;color:var(--red)}
.card .name{position:absolute;left:30px;top:238px;font-size:15px;color:#333}
.card .prices{position:absolute;left:30px;top:272px;font-size:13px}
.card .prices b{color:var(--red);font-weight:600}
.card .prices s{color:#aaa;margin-left:10px}

/* banner */
.xmas{left:112px;top:2133px;width:976px;height:232px;background:#dff4d2}
.xmas h2{position:absolute;left:96px;top:20px;font-family:"Roboto",sans-serif;font-weight:900;font-size:60px;line-height:58px;color:var(--red)}
.xmas h2 span{color:#111}
.xmas p{position:absolute;left:98px;top:198px;font-size:14px;color:#333}
.xmas .art{position:absolute;left:540px;top:22px;width:380px;height:210px;background:linear-gradient(90deg,#b9e3a2,#8dd0e8 60%,#c23b4a)}
.xmas .close{position:absolute;right:18px;top:16px;width:18px;height:18px;border-radius:50%;background:#222}

/* partners */
.partner{top:2453px;width:184px;height:116px;border:1px solid var(--line);display:flex;align-items:center;justify-content:center}
.partner i{width:90px;height:40px;background:#ddd;border-radius:4px}

/* blog */
.see-all{right:112px;top:3118px;font-size:12px;color:var(--red);text-decoration:underline}
.blog-img{background:linear-gradient(135deg,#9a8e7e,#d7ccbc)}
.post{text-align:center;padding-top:62px}
.post .date{font-size:12px;color:#555}
.post .date::before{content:"";display:inline-block;width:10px;height:10px;border:2px solid var(--red);border-radius:2px;margin-right:8px;vertical-align:-1px}
.post h4{font-size:17px;font-weight:600;line-height:34px;margin-top:24px;color:#222}
.post .more{display:inline-block;margin-top:22px;font-size:12px;font-weight:700;color:var(--red)}

/* newsletter */
.news{top:3843px;left:0;width:1200px;height:110px;background:var(--red);color:#fff}
.news h3{position:absolute;left:164px;top:40px;font-family:"Roboto",sans-serif;font-weight:700;font-size:24px;text-transform:uppercase}
.news .ico{position:absolute;left:112px;top:38px}
.news p{position:absolute;left:424px;top:46px;font-size:13px}
.news form{position:absolute;left:643px;top:33px;width:445px;height:44px;display:flex}
.news input{flex:1;border:0;padding:0 18px;font-family:inherit;font-size:12px;color:#999}
.news button{width:106px;border:0;background:var(--dark);color:#fff;font-weight:700;font-size:12px;font-family:inherit}

/* footer */
.footer{top:3953px;left:0;width:1200px;height:373px;background:var(--footer);color:#fff}
.footer h5{font-family:"Roboto",sans-serif;font-size:16px;font-weight:700}
.cats{left:112px;top:72px;width:640px}
.cats p{margin-top:22px;font-size:13px;line-height:34px;color:#ddd}
.cats p span{color:#777;margin:0 8px}
.follow{left:112px;top:242px}
.social{display:flex;gap:28px;margin-top:20px;font-size:13px;color:#ddd}
.social span::before{content:"";display:inline-block;width:10px;height:10px;border-radius:50%;background:var(--red);margin-right:8px}
.says{left:815px;top:72px;width:280px}
.says blockquote{margin-top:20px;font-style:italic;font-size:13px;line-height:26px;color:#ccc}
.says .who{margin-top:12px;font-size:13px;color:var(--red)}
.says .role{font-size:12px;color:#aaa;margin-top:4px;font-style:italic}
.says .dots{margin-top:20px}
.says .dots i{background:#555}
.says .dots i.on{background:var(--red)}

/* bottom */
.bottom{top:4326px;left:0;width:1200px;height:118px}
.bottom .copy{left:112px;top:50px;font-size:12px;color:#555}
.bottom .brand{left:0;width:1200px;top:40px;justify-content:center;font-size:30px}
.cards{right:112px;top:50px;display:flex;gap:12px}
.cards i{width:32px;height:20px;background:#c9c9c9;border-radius:3px}
</style>
</head>
<body>

<header class="abs topbar">
  <div class="abs links">LOCATION &amp; CONTACTS<span>|</span>LOGIN<span>|</span>BECOME A NEW CUSTOMER</div>
  <div class="abs prefs"><span><i class="flag"></i>LANG ▾</span><span>$ CURRENCY ▾</span></div>
</header>

<div class="abs brand"><span class="mark"></span>Tallow Finch</div>
<form class="abs search"><input value="SEARCH..."><button type="button" aria-label="Search"><svg width="20" height="20" viewBox="0 0 20 20"><circle cx="8" cy="8" r="6" fill="none" stroke="#fff" stroke-width="2.5"/><path d="M12.5 12.5l5 5" stroke="#fff" stroke-width="2.5"/></svg></button></form>
<svg class="abs account" width="38" height="38" viewBox="0 0 38 38" aria-label="Account"><circle cx="19" cy="19" r="17" fill="none" stroke="#222" stroke-width="2"/><circle cx="19" cy="15" r="6" fill="#222"/><path d="M8 30c3-7 19-7 22 0" fill="#222"/></svg>
<div class="abs cart"><svg width="38" height="34" viewBox="0 0 38 34"><path d="M2 4h6l5 20h18l4-14H11" fill="none" stroke="#222" stroke-width="2.5"/><circle cx="15" cy="30" r="3" fill="#222"/><circle cx="28" cy="30" r="3" fill="#222"/></svg><span class="badge">0</span><span>0-ITEMS</span></div>

<nav class="abs nav">
  <ul>
    <li class="shop">SHOP BY BRAND ▾</li><li>ALL DEPARTMENTS</li><li>NEW ARRIVALS</li><li>CLEANING SUPPLIES</li><li>COOKWARE AND BAKING</li><li>CRAFTS AND HOBBIES</li><li>FOOD</li>
  </ul>
  <svg class="abs more" width="6" height="18" viewBox="0 0 6 18"><circle cx="3" cy="3" r="2" fill="#fff"/><circle cx="3" cy="9" r="2" fill="#fff"/><circle cx="3" cy="15" r="2" fill="#fff"/></svg>
</nav>

<section class="abs hero" role="img" aria-label="Glass jars filled with gold and pearl beads">
  <p class="abs kicker">Sed ut perspiciatis unde omnis iste natus error sit voluptatem</p>
  <h1 class="abs">Beaded<br>Glass Jars</h1>
  <span class="abs arrow-btn" style="left:24px;top:206px"><svg width="12" height="12"><path d="M8 1L3 6l5 5" fill="none" stroke="#fff" stroke-width="2"/></svg></span>
  <span class="abs arrow-btn" style="left:1130px;top:206px"><svg width="12" height="12"><path d="M4 1l5 5-5 5" fill="none" stroke="#fff" stroke-width="2"/></svg></span>
  <div class="abs dots" style="left:572px;top:452px"><i class="on"></i><i></i><i></i><i></i></div>
</section>

<a class="abs promo dark"><h3>Health and<br>Beauty</h3><p>Sed ut perspiciatis</p><div class="art" role="img" aria-label="Spray bottles and beauty products" style="background:linear-gradient(135deg,#333,#777 50%,#c0392b)"></div></a>
<a class="abs promo red"><h3>Cookware and<br>Baking</h3><p>Sed ut perspiciatis</p><div class="art" role="img" aria-label="Seasonal sale badge" style="background:linear-gradient(135deg,#f06a70,#fbd5d7)"></div></a>

<aside class="abs services">
  <div class="service"><span class="ico"><svg width="22" height="16"><rect x="1" y="2" width="13" height="10" fill="#e3101b"/><path d="M14 5h4l3 4v3h-7z" fill="#e3101b"/><circle cx="5" cy="13" r="2" fill="#e3101b"/><circle cx="17" cy="13" r="2" fill="#e3101b"/></svg></span><div><h4>Free Shipping</h4><p>Delivery All Over The World Free</p></div></div>
  <div class="service"><span class="ico"><svg width="22" height="22"><path d="M3 13a8 8 0 0 1 16 0" fill="none" stroke="#e3101b" stroke-width="2.5"/><rect x="2" y="12" width="4" height="7" rx="1" fill="#e3101b"/><rect x="16" y="12" width="4" height="7" rx="1" fill="#e3101b"/></svg></span><div><h4>24/7 Online Help</h4><p>Delivery All Over The World Free</p></div></div>
  <div class="service"><span class="ico"><svg width="22" height="22"><path d="M4 11a7 7 0 1 0 2-5" fill="none" stroke="#e3101b" stroke-width="2.5"/><path d="M2 3v5h5" fill="none" stroke="#e3101b" stroke-width="2.5"/></svg></span><div><h4>Money Return</h4><p>Delivery All Over The World Free</p></div></div>
  <div class="service"><span class="ico"><svg width="22" height="22"><path d="M2 11L11 2h9v9l-9 9z" fill="#e3101b"/><circle cx="15" cy="7" r="2" fill="#fff"/></svg></span><div><h4>User Discount</h4><p>Delivery All Over The World Free</p></div></div>
</aside>

<h2 class="abs section-title" style="left:418px;top:1068px">Deal Of The Week</h2>
<div class="abs deal-nav">Previous Deal <b>|</b> <b>Next Deal</b></div>
<article class="abs deal-card">
  <div class="abs pic" role="img" aria-label="Black trigger spray bottle with patterned label"></div>
  <h3 class="abs">Sprayer Bottle 400ml Salon</h3>
  <div class="abs stars" style="left:345px;top:132px">★★★★★</div>
  <div class="abs price">$56.89</div>
  <p class="abs desc">Sed ut perspiciatis unde omnis iste natus error sit voluptatem accusant doloremque</p>
  <div class="abs countdown"><div><span>139</span>Days</div><div><span>14</span>Hours</div><div><span>50</span>Mins</div><div><span>57</span>Secs</div></div>
</article>

<div class="abs tabs"><span class="on">New Arrival</span><span>Best Seller</span></div>
<div class="abs pager" style="top:1654px"><i class="on">‹</i><i>›</i></div>

<div class="abs card" style="left:112px;top:1730px"><div class="pic" role="img" aria-label="Set of polka dot paper cups" style="background:linear-gradient(135deg,#f7e1e8,#cfe3f7)"></div><span class="off">10% Off</span><span class="name">Voluptates repudiandae</span><span class="prices"><b>$122.00</b><s>$140.00</s></span></div>
<div class="abs card" style="left:364px;top:1730px"><div class="pic" role="img" aria-label="Packaged round cake boards" style="background:linear-gradient(135deg,#333,#e8d6a8)"></div><span class="name">Architecto beatae</span><span class="prices"><b>$122.00</b><s>$140.00</s></span></div>
<div class="abs card" style="left:616px;top:1730px"><div class="pic" role="img" aria-label="Grey swing-lid waste bin" style="background:linear-gradient(135deg,#ececec,#9a9a9a)"></div><span class="off">10% Off</span><span class="name">Exercitatione</span><span class="prices"><b>$122.00</b><s>$140.00</s></span></div>
<div class="abs card" style="left:866px;top:1730px"><div class="pic" role="img" aria-label="Stacked food containers with blue lids" style="background:linear-gradient(135deg,#3140b8,#e4e6f5)"></div><span class="off">10% Off</span><span class="name">Neque porro quisqua</span><span class="prices"><b>$122.00</b><s>$140.00</s></span></div>

<section class="abs xmas">
  <h2>CHRISTMAS<br><span>TUMBLERS<br>&amp; JARS</span></h2>
  <p>Double walled</p>
  <div class="art" role="img" aria-label="Festive tumblers and mason jars with straws"></div>
  <span class="close"></span>
</section>

<div class="abs partner" style="left:112px"><i></i></div>
<div class="abs partner" style="left:310px"><i></i></div>
<div class="abs partner" style="left:508px"><i></i></div>
<div class="abs partner" style="left:706px"><i></i></div>
<div class="abs partner" style="left:904px"><i></i></div>

<h2 class="abs section-title" style="left:112px;top:2643px">Featured Products</h2>
<div class="abs pager" style="top:2646px"><i class="on">‹</i><i>›</i></div>

<div class="abs card" style="left:112px;top:2720px"><div class="pic" role="img" aria-label="Stack of patterned storage tins" style="background:linear-gradient(135deg,#1f3d7a,#e6a24d)"></div><span class="off">10% Off</span><span class="name">Voluptates repudiandae</span><span class="prices"><b>$122.00</b><s>$140.00</s></span></div>
<div class="abs card" style="left:364px;top:2720px"><div class="pic" role="img" aria-label="Clear containers with pastel lids" style="background:linear-gradient(135deg,#9bd4f2,#f3a6d3)"></div><span class="name">Architecto beatae</span><span class="prices"><b>$122.00</b><s>$140.00</s></span></div>
<div class="abs card" style="left:616px;top:2720px"><div class="pic" role="img" aria-label="White bucket with lid" style="background:linear-gradient(135deg,#fafafa,#cfcfcf)"></div><span class="off">10% Off</span><span class="name">Exercitatione</span><span class="prices"><b>$122.00</b><s>$140.00</s></span></div>
<div class="abs card" style="left:866px;top:2720px"><div class="pic" role="img" aria-label="Coloured trigger spray bottles" style="background:linear-gradient(135deg,#7a6fd6,#c9e4f5)"></div><span class="name">Neque porro quisqua</span><span class="prices"><b>$122.00</b><s>$140.00</s></span></div>

<h2 class="abs section-title" style="left:112px;top:3110px">From the Blog</h2>
<a class="abs see-all">See All Blogs</a>

<div class="abs blog-img" style="left:112px;top:3191px;width:282px;height:276px;background:linear-gradient(135deg,#d8c9b4,#f1c52c)" role="img" aria-label="Floor being cleaned with a mop and yellow bucket"></div>
<article class="abs post" style="left:112px;top:3467px;width:282px;height:278px"><div class="date">22/09/2018</div><h4>Urna Pretium Elit Mauris<br>Curs dicta suntus</h4><span class="more">Read More ➜</span></article>
<article class="abs post" style="left:394px;top:3191px;width:285px;height:276px;padding-top:62px"><div class="date">22/09/2018</div><h4>Urna Pretium Elit Mauris<br>Curs dicta suntus</h4><span class="more">Read More ➜</span></article>
<div class="abs blog-img" style="left:394px;top:3467px;width:285px;height:278px;background:linear-gradient(135deg,#d6d6d6,#e2501e 60%,#f2f2f2)" role="img" aria-label="Orange cast iron casserole pot"></div>
<div class="abs blog-img" style="left:694px;top:3191px;width:394px;height:276px;background:linear-gradient(135deg,#2e3f5c,#9cc3df 60%,#6b5a43)" role="img" aria-label="Water poured into a glass"></div>
<div class="abs" style="left:694px;top:3467px;width:106px;height:278px;background:linear-gradient(#4a3a2b,#2a221b)" role="img" aria-label="Wooden table surface"></div>
<article class="abs post" style="left:800px;top:3467px;width:288px;height:278px"><div class="date">22/09/2018</div><h4>Urna Pretium Elit Mauris<br>Curs dicta suntus</h4><span class="more">Read More ➜</span></article>

<section class="abs news">
  <svg class="ico" width="36" height="32" viewBox="0 0 36 32"><path d="M2 12L18 2l16 10v18H2z" fill="none" stroke="#fff" stroke-width="2.5"/><path d="M2 12l16 11 16-11" fill="none" stroke="#fff" stroke-width="2.5"/></svg>
  <h3>Get Daily Update</h3>
  <p>Join us for get latest updates</p>
  <form><input value="Enter Email..."><button type="button">SUBSCRIBE</button></form>
</section>

<footer class="abs footer">
  <div class="abs cats">
    <h5>Categories</h5>
    <p>Shop By Brand<span>/</span>All Departments<span>/</span>New Arrivals<span>/</span>Cleaning Supplies<span>/</span>Cookware And Baking<br>Crafts And Hobbies<span>/</span>Food<span>/</span>Glassware<span>/</span>Hardware<span>/</span>Health And Beauty<span>/</span>Home Accessories<br>Kitchenware<span>/</span>Plasticware<span>/</span>Seasonal<span>/</span>Stainless Steel<span>/</span>Tableware<span>/</span>Opportunity Buys</p>
  </div>
  <div class="abs follow">
    <h5>Follow us</h5>
    <div class="social"><span>Friendbook</span><span>Chirpline</span><span>Snapframe</span><span>Reelcast</span></div>
  </div>
  <div class="abs says">
    <h5>What they says</h5>
    <blockquote>Lorem ipsum dolor sit amet, consectetur adipiscing elit, sed do eiusmod tempor incididunt ut labore et dolore magna aliqua.</blockquote>
    <div class="who">- JOHN DOE</div>
    <div class="role">Customer</div>
    <div class="dots"><i class="on"></i><i></i><i></i></div>
  </div>
</footer>

<div class="abs bottom">
  <div class="abs copy">© 2018 Companyname All Rights Reserved</div>
  <div class="abs brand"><span class="mark"></span>Tallow Finch</div>
  <div class="abs cards"><i></i><i></i><i></i><i></i><i></i></div>
</div>

</body>
</html>
```